Web page for Marcus Penrose Chartered Tax Adviser

I need to take the basic web page that I have created and "Brand it" to be compatible with the corporate logo and stationery created for me by other Pixel Guild designers.
I will need a watermark as well as a distinctive home page and then a branded general page for content including a series of Blogs.

Target Market(s)

My practice deals with expatriates including those looking to invest in Australia.

Industry/Entity Type

Crowd

Font styles to use
Other font styles liked:
• Per logo

Requirements
Must have
• Besides the homepage I will need a general page for content, branded in the same style as the letterheads.
Nice to have
• A watermark to go with the blogs and news content.

```html
<!DOCTYPE html>
<html lang="en">
<head>
<meta charset="utf-8">
<title>Marcus Penrose Chartered Tax Adviser</title>
<link href="https://fonts.googleapis.com/css2?family=Marcellus+SC&family=Lato:wght@400;700&family=Noto+Serif:ital,wght@1,700&family=Roboto+Condensed:wght@400&display=swap" rel="stylesheet">
<style>
:root{
  --navy:#0f3356;
  --navy-deep:#0a2440;
  --steel:#2e5b7e;
  --steel-light:#4b7a9c;
  --ink:#333a40;
  --heading:#1d2a36;
  --accent:#1e4f7d;
  --grey-bg:#f1f1f1;
  --line:#d6d9dc;
  --white:#ffffff;
  --icon:#4a4f55;
  --footer:#17426a;
}
*{box-sizing:border-box;margin:0;padding:0}
html,body{width:1200px;height:2172px;overflow:hidden}
body{position:relative;background:var(--white);font-family:"Lato",sans-serif;color:var(--ink)}

/* navigation */
.main-nav{position:absolute;left:0;top:0;width:1200px;height:40px;background:linear-gradient(#1a4870,var(--navy));display:flex;justify-content:center}
.main-nav a{font-family:"Marcellus SC",serif;color:var(--white);font-size:19px;text-decoration:none;line-height:40px;padding:0 40px;border-right:1px solid rgba(255,255,255,.15)}
.main-nav a:last-child{border-right:none}

/* hero */
.hero{position:absolute;left:0;top:40px;width:1200px;height:778px;overflow:hidden}
.hero-photo{position:absolute;inset:0;background:
  radial-gradient(ellipse 260px 420px at 860px 380px,rgba(20,36,58,.85),rgba(20,36,58,0) 70%),
  radial-gradient(ellipse 380px 300px at 420px 330px,rgba(235,244,250,.75),rgba(235,244,250,0) 70%),
  radial-gradient(ellipse 300px 120px at 650px 560px,rgba(30,50,75,.55),rgba(30,50,75,0) 70%),
  radial-gradient(ellipse 240px 500px at 1120px 380px,rgba(40,70,100,.6),rgba(40,70,100,0) 70%),
  linear-gradient(100deg,#c7d6e3 0%,#9eb8cf 30%,#7b9ab6 55%,#5a7c9a 75%,#8aa8c2 90%,#6a8aa6 100%)}
.hero-curves{position:absolute;inset:0}
.brand{position:absolute;left:132px;top:26px;display:flex;align-items:center;gap:16px}
.brand-mark{width:70px;height:70px;background:var(--accent)}
.brand-name{font-family:"Marcellus SC",serif;color:var(--accent);font-size:46px;line-height:1}
.brand-name span{display:block;font-size:21px;letter-spacing:5px;margin-top:6px}
.header-phone{position:absolute;left:912px;top:14px;display:flex;align-items:center;gap:10px;font-weight:700;font-size:22px;color:var(--navy)}
.tagline{position:absolute;left:138px;top:675px;font-family:"Noto Serif",serif;font-style:italic;font-weight:700;font-size:35px;line-height:48px;color:var(--white)}
.slider-dots{position:absolute;left:950px;top:744px;display:flex;gap:13px}
.slider-dots i{width:18px;height:18px;border-radius:50%;background:var(--white)}
.slider-dots i.active{background:var(--steel-light);border:2px solid var(--white)}

/* services */
.services{position:absolute;left:0;top:818px;width:1200px;height:317px;background:linear-gradient(var(--steel),var(--navy-deep))}
.section-title{font-family:"Marcellus SC",serif;font-weight:400;color:var(--white);font-size:37px;text-align:center;position:absolute;left:0;width:1200px;top:20px}
.services .rule{position:absolute;left:160px;top:75px;width:910px;border-top:1px dashed rgba(255,255,255,.35)}
.service{position:absolute;top:103px;width:170px;text-align:center;margin-left:-85px}
.service-icon{width:122px;height:122px;margin:0 auto;border-radius:50%;background:var(--white);border:5px solid #c9d0d6;display:flex;align-items:center;justify-content:center}
.service p{font-family:"Roboto Condensed",sans-serif;color:var(--white);font-size:20px;line-height:22px;margin-top:14px}
.arrow{position:absolute;top:152px}

/* welcome */
.welcome{position:absolute;left:134px;top:1170px;width:590px}
h2.block-title{font-family:"Marcellus SC",serif;font-weight:400;color:var(--heading);font-size:31px;padding-bottom:10px;border-bottom:1px solid var(--line)}
h2.block-title em{font-style:normal;color:var(--accent)}
h2.block-title small{font-family:"Lato",sans-serif;font-weight:700;font-size:17px;color:var(--heading)}
.welcome p{font-size:14.5px;line-height:21px;margin-top:14px;color:#3b4249}
.btn{display:inline-block;background:var(--navy);color:var(--white);font-weight:700;font-size:13px;padding:7px 14px;border-radius:4px;box-shadow:0 2px 3px rgba(0,0,0,.35);text-transform:uppercase}
.welcome .btn{margin-top:14px}
.divider-v{position:absolute;left:751px;top:1190px;height:240px;border-left:1px solid var(--line)}
.inquiry{position:absolute;left:778px;top:1170px;width:290px}
.inquiry .field{border:1px solid #ccd1d5;height:29px;margin-top:10px;font-size:12px;color:#9aa2a9;padding:7px 10px}
.inquiry .field:first-of-type{margin-top:16px}
.inquiry .field.msg{height:64px}
.inquiry .btn{margin-top:12px;padding:7px 22px}

/* info band */
.info-band{position:absolute;left:0;top:1481px;width:1200px;height:400px;background:var(--grey-bg)}
.col{position:absolute;top:1512px}
.col h2.block-title{font-size:27px}
.team-photo{width:248px;height:117px;margin-top:18px;background:linear-gradient(180deg,#e9eef2 0%,#c9d6e1 45%,#8aa3b9 100%);border:3px solid var(--white);box-shadow:0 0 2px rgba(0,0,0,.3)}
.team p{font-size:13.5px;line-height:18px;margin-top:8px}
.team .btn{margin-top:14px}
.col-head{display:flex;justify-content:space-between;align-items:flex-end;border-bottom:1px solid var(--line)}
.col-head h2.block-title{border:none}
.col-head span{color:#666;font-size:22px;padding-bottom:12px;letter-spacing:2px}
.news-item{display:flex;gap:18px;margin-top:22px;padding-bottom:12px;border-bottom:1px solid #e1e3e5}
.date{width:51px;text-align:center;flex:none}
.date b{display:block;background:#5b5f63;color:var(--white);font-size:22px;line-height:30px}
.date span{display:block;background:var(--white);border:1px solid #ccc;font-size:12px;font-weight:700;line-height:22px}
.news-item h3{font-size:13px;font-weight:700;color:var(--heading)}
.news-item p,.blog-item p{font-size:12.5px;line-height:15px;color:#3b4249;margin-top:4px}
.blog-item{display:flex;gap:12px;margin-top:20px}
.avatar{width:65px;height:65px;flex:none;border:2px solid var(--white);box-shadow:0 0 3px rgba(0,0,0,.35);background:linear-gradient(#e2a07a,#c0604a)}
.blog-item h3{font-size:13.5px;font-weight:700;color:var(--accent)}
.blog-item .posted{font-style:italic;font-size:12.5px;color:var(--accent);margin-top:2px}

/* footer */
.footer-curve{position:absolute;left:0;top:1780px;width:1200px;height:160px}
.footer{position:absolute;left:0;top:1935px;width:1200px;height:201px;background:var(--footer)}
.footer-col h4{font-weight:700;color:var(--white);font-size:16px}
.footer-col{position:absolute;top:1945px;color:var(--white);font-size:13px}
.footer-col ul{list-style:none;margin-top:14px}
.footer-col li{line-height:24px}
.footer-col li::before{content:"»";margin-right:14px}
.contact-row{display:flex;gap:12px;align-items:flex-start;margin-top:10px;line-height:17px}
.contact-row svg{flex:none;margin-top:2px}
.map{position:absolute;left:539px;top:1982px;width:203px;height:123px;background:linear-gradient(135deg,#e6dcc4,#c9d7cf 50%,#a9c4dc);border:2px solid var(--white)}
.subscribe p{margin-top:12px;line-height:17px;width:250px}
.subscribe .form{display:flex;margin-top:12px}
.subscribe .form div{width:152px;height:33px;background:var(--white);color:#444;font-size:13px;padding:9px 8px}
.subscribe .form span{width:94px;height:33px;background:#1b1b1b;font-weight:700;font-size:13px;text-align:center;line-height:33px}
.social{display:flex;gap:8px;align-items:center;margin-top:14px}
.social i{width:33px;height:33px;border-radius:4px;background:#3a7fc4}
.copyright{position:absolute;left:0;top:2136px;width:1200px;height:36px;background:#0b0b0b;color:#ddd;font-size:12px;text-align:center;line-height:36px}
</style>
</head>
<body>

<nav class="main-nav">
  <a>Home</a><a>Services</a><a>News</a><a>Blog</a><a>About Us</a><a>Careers</a><a>Contact Us</a>
</nav>

<header class="hero">
  <div class="hero-photo" role="img" aria-label="Businessman standing by a window in a city office with laptop on desk"></div>
  <svg class="hero-curves" width="1200" height="778" viewBox="0 0 1200 778">
    <defs>
      <linearGradient id="topWash" x1="0" y1="0" x2="1" y2="0">
        <stop offset="0" stop-color="#ffffff"/>
        <stop offset="0.6" stop-color="#f3f5f7"/>
        <stop offset="1" stop-color="#d9dfe5"/>
      </linearGradient>
      <linearGradient id="bottomBand" x1="0" y1="0" x2="0" y2="1">
        <stop offset="0" stop-color="#1d4a72"/>
        <stop offset="1" stop-color="#0a2440"/>
      </linearGradient>
    </defs>
    <path d="M0 0 H1200 V40 C900 60 620 90 440 170 C330 220 150 225 0 205 Z" fill="url(#topWash)"/>
    <path d="M190 225 C330 222 420 180 520 130 C600 95 720 80 800 78 C700 95 600 130 510 175 C420 215 320 232 190 225 Z" fill="#0f3356"/>
    <path d="M0 700 C250 650 500 640 800 655 C950 662 1100 650 1200 630 V778 H0 Z" fill="url(#bottomBand)" opacity="0.92"/>
    <path d="M80 690 C300 650 560 640 820 650 C980 656 1100 648 1200 632" stroke="#b9c0c7" stroke-width="6" fill="none"/>
  </svg>
  <div class="brand">
    <div class="brand-mark"></div>
    <div class="brand-name">Marcus Penrose<span>Chartered Tax Adviser</span></div>
  </div>
  <div class="header-phone">
    <svg width="22" height="22" viewBox="0 0 24 24"><circle cx="12" cy="12" r="11" fill="none" stroke="#0f3356" stroke-width="2"/><path d="M8 6l2 0 1 3-1.5 1c.7 1.6 1.9 2.8 3.5 3.5l1-1.5 3 1v2c0 1-1 1.5-2 1.5-4.5-.5-8-4-8.5-8.5 0-1 .5-2 1.5-2z" fill="#0f3356"/></svg>
    123-456-7890
  </div>
  <div class="tagline">Specialist Advice,<br>&nbsp;Personal Service</div>
  <div class="slider-dots"><i class="active"></i><i></i><i></i><i></i></div>
</header>

<section class="services">
  <h2 class="section-title">Our Services</h2>
  <div class="rule"></div>
  <svg class="arrow" style="left:100px" width="18" height="30" viewBox="0 0 18 30"><path d="M14 3 L4 15 L14 27" stroke="#fff" stroke-width="3" fill="none"/></svg>
  <svg class="arrow" style="left:1085px" width="18" height="30" viewBox="0 0 18 30"><path d="M4 3 L14 15 L4 27" stroke="#fff" stroke-width="3" fill="none"/></svg>

  <div class="service" style="left:201px"><div class="service-icon">
    <svg width="60" height="60" viewBox="0 0 60 60"><circle cx="25" cy="25" r="14" fill="none" stroke="#4a4f55" stroke-width="4"/><path d="M35 35 L50 50" stroke="#4a4f55" stroke-width="7" stroke-linecap="round"/><circle cx="25" cy="25" r="5" fill="#4a4f55"/></svg>
  </div><p>Audit &amp;<br>Assurance</p></div>

  <div class="service" style="left:358px"><div class="service-icon">
    <svg width="60" height="60" viewBox="0 0 60 60"><circle cx="22" cy="20" r="8" fill="#4a4f55"/><path d="M8 46 C8 34 14 30 22 30 C30 30 36 34 36 46 Z" fill="#4a4f55"/><circle cx="40" cy="25" r="7" fill="#6a7077"/><path d="M28 50 C28 40 33 36 40 36 C47 36 52 40 52 50 Z" fill="#6a7077"/></svg>
  </div><p>Business<br>Advisory</p></div>

  <div class="service" style="left:518px"><div class="service-icon">
    <svg width="60" height="60" viewBox="0 0 60 60"><rect x="14" y="8" width="32" height="44" rx="3" fill="#4a4f55"/><rect x="18" y="12" width="24" height="9" fill="#fff"/><g fill="#fff"><rect x="18" y="25" width="6" height="5"/><rect x="27" y="25" width="6" height="5"/><rect x="36" y="25" width="6" height="5"/><rect x="18" y="33" width="6" height="5"/><rect x="27" y="33" width="6" height="5"/><rect x="36" y="33" width="6" height="5"/><rect x="18" y="41" width="6" height="5"/><rect x="27" y="41" width="6" height="5"/><rect x="36" y="41" width="6" height="5"/></g></svg>
  </div><p style="margin-top:25px">Taxation</p></div>

  <div class="service" style="left:673px"><div class="service-icon">
    <svg width="60" height="60" viewBox="0 0 60 60"><path d="M6 14 H22 L26 19 H46 V44 H6 Z" fill="#4a4f55"/><circle cx="40" cy="38" r="9" fill="#fff" stroke="#4a4f55" stroke-width="4"/><path d="M46 44 L54 52" stroke="#4a4f55" stroke-width="5" stroke-linecap="round"/></svg>
  </div><p>Business Recovery<br>and Insolvency</p></div>

  <div class="service" style="left:834px"><div class="service-icon">
    <svg width="60" height="60" viewBox="0 0 60 60"><path d="M10 22 H44" stroke="#4a4f55" stroke-width="5"/><path d="M38 13 L50 22 L38 31 Z" fill="#4a4f55"/><path d="M50 40 H16" stroke="#6a7077" stroke-width="5"/><path d="M22 31 L10 40 L22 49 Z" fill="#6a7077"/></svg>
  </div><p>Corporate<br>Finance</p></div>

  <div class="service" style="left:995px"><div class="service-icon">
    <svg width="60" height="60" viewBox="0 0 60 60"><circle cx="30" cy="30" r="24" fill="#4a4f55"/><circle cx="30" cy="30" r="12" fill="none" stroke="#fff" stroke-width="5"/><rect x="26" y="28" width="8" height="26" fill="#4a4f55"/><rect x="28" y="32" width="4" height="14" fill="#fff"/></svg>
  </div><p>Wealth<br>Creation</p></div>
</section>

<section class="welcome">
  <h2 class="block-title">Welcome to <em>Marcus Penrose</em> <small>Charted tax adviser</small></h2>
  <p>Lorem ipsum dolor sit amet, consectetuer adipiscing elit, sed diam nonummy nibh euismod tincidunt ut laoreet dolore magna aliquam erat volutpat. Ut wisi enim ad minim veniam, quis nostrud exerci tation ullamcorper suscipit lobortis nisl ut aliquip ex ea commodo consequat. Duis autem vel eum iriure dolor in hendrerit in vulputate velit esse molestie consequat, vel illum dolore eu feugiat nulla facilisis at vero eros et accumsan et iusto odio dignissim qui blandit tincidunt ut laoreet dolore magna aliquam erat volutpat. Ut wisi enim ad minim veniam, quis praesent luptatum zzril delenit augue duis dolore te feugait nulla facilisi dolore eu feugiat nulla facilisis at vero eros et accumsan et iusto odio dignissim qui blandit.</p>
  <span class="btn">Read More</span>
</section>
<div class="divider-v"></div>
<section class="inquiry">
  <h2 class="block-title">Quick Inquiry</h2>
  <div class="field">Name</div>
  <div class="field">Mobile Number</div>
  <div class="field">Email</div>
  <div class="field msg">Message</div>
  <span class="btn">Submit</span>
</section>

<div class="info-band"></div>

<section class="col team" style="left:134px;width:250px">
  <h2 class="block-title">Meet Our Team</h2>
  <div class="team-photo" role="img" aria-label="Group photo of the advisory team"></div>
  <p>Lorem ipsum dolor sit amet, consdfgisc etuer adipiscing elit, sed diam nonummy nibh euismod tincidunt ut</p>
  <span class="btn">Read More</span>
</section>

<section class="col news" style="left:449px;width:265px">
  <div class="col-head"><h2 class="block-title">Latest News</h2><span>‹›</span></div>
  <div class="news-item"><div class="date"><b>30</b><span>DEC</span></div><div><h3>Euismod Tincidunt Ut Laoreet</h3><p>Lorem ipsum dolor sit amasgiget conetuge sed diay nibhsdhgidl tincidunt ut laoreet</p></div></div>
  <div class="news-item"><div class="date"><b>01</b><span>JAN</span></div><div><h3>Euismod Tincidunt Ut Laoreet</h3><p>Lorem ipsum dolor sit amasgiget conetuge sed diay nibhsdhgidl tincidunt ut laoreet</p></div></div>
  <div class="news-item" style="border:none"><div class="date"><b>02</b><span>JAN</span></div><div><h3>Euismod Tincidunt Ut Laoreet</h3><p>Lorem ipsum dolor sit amasgiget conetuge sed diay nibhsdhgidl tincidunt ut laoreet</p></div></div>
</section>

<section class="col blog" style="left:778px;width:290px">
  <div class="col-head"><h2 class="block-title">Recent Blog Posts</h2><span>‹›</span></div>
  <div class="blog-item"><div class="avatar" role="img" aria-label="Author portrait"></div><div><h3>Lorem ipsum dolor sit amet</h3><div class="posted"><b>Posted :</b> 29 Dec 2014</div><p>Lorem ipsum dolor consectetuer Lorem ipsum dolor sit amet</p></div></div>
  <div class="blog-item"><div class="avatar" role="img" aria-label="Author portrait" style="background:linear-gradient(#8a6a55,#d7a68c)"></div><div><h3>Lorem ipsum dolor sit amet</h3><div class="posted"><b>Posted :</b> 29 Dec 2014</div><p>Lorem ipsum dolor consectetuer Lorem ipsum dolor sit amet</p></div></div>
  <div class="blog-item"><div class="avatar" role="img" aria-label="Author portrait"></div><div><h3>Lorem ipsum dolor sit amet</h3><div class="posted"><b>Posted :</b> 29 Dec 2014</div><p>Lorem ipsum dolor consectetuer Lorem ipsum dolor sit amet</p></div></div>
</section>

<svg class="footer-curve" width="1200" height="160" viewBox="0 0 1200 160">
  <path d="M0 60 C200 150 500 160 800 120 C950 100 1100 60 1200 30 V160 H0 Z" fill="#17426a"/>
  <path d="M0 35 C150 120 420 150 720 125 C900 110 1080 70 1200 30 L1200 42 C1080 80 900 122 720 136 C420 160 150 130 0 55 Z" fill="#b8bec4"/>
</svg>
<footer class="footer"></footer>

<section class="footer-col" style="left:132px">
  <h4>Quick Links</h4>
  <ul><li>Home</li><li>About US</li><li>Services</li><li>Solutions</li><li>Blog</li><li>Contact Us</li></ul>
</section>

<section class="footer-col" style="left:328px;width:200px">
  <h4>Contact Details</h4>
  <div class="contact-row" style="margin-top:16px"><svg width="14" height="18" viewBox="0 0 14 18"><path d="M7 0a7 7 0 0 1 7 7c0 5-7 11-7 11S0 12 0 7a7 7 0 0 1 7-7z" fill="#fff"/><circle cx="7" cy="7" r="2.5" fill="#17426a"/></svg><span>Vestibulum tristique ati eros Maecenas elit lion Street no:2</span></div>
  <div class="contact-row"><svg width="14" height="14" viewBox="0 0 24 24"><path d="M5 2l4 0 2 5-3 2c1.3 3 3.7 5.4 7 7l2-3 5 2v4c0 1.5-1.5 2.5-3 2.5C10 21 3 14 2.5 5c0-1.5 1-3 2.5-3z" fill="#fff"/></svg><span>123-456-7890</span></div>
  <div class="contact-row"><svg width="14" height="16" viewBox="0 0 14 16"><rect x="2" y="0" width="10" height="16" rx="2" fill="#fff"/><rect x="4" y="2" width="6" height="10" fill="#17426a"/></svg><span>456-789-1234</span></div>
  <div class="contact-row"><svg width="14" height="12" viewBox="0 0 14 12"><rect width="14" height="12" fill="#fff"/><path d="M0 0 L7 6 L14 0" stroke="#17426a" fill="none"/></svg><span>info@marcuspenrose.com</span></div>
</section>
<div class="map" role="img" aria-label="Street map showing office location"></div>

<section class="footer-col subscribe" style="left:820px">
  <h4>Subscribe for Newsletter</h4>
  <p>Lorem ipsum dolor sit a conur ut adiisci dolor sit a constetur ut adiisci</p>
  <div class="form"><div>Enter your email</div><span>SUBSCRIBE</span></div>
  <div class="social">Follow Us On :<i role="img" aria-label="Social profile"></i><i role="img" aria-label="Social profile" style="background:#4aa3df"></i><i role="img" aria-label="Social profile" style="background:#2a6aa8"></i><i role="img" aria-label="News feed" style="background:#e8912a"></i></div>
</section>

<div class="copyright">Copyright © 2014 Marcus Penrose. All rights reserved</div>

</body>
</html>
```